Web design for sitter site

We will be launching a sitter site in the coming months that focuses on sitters for children. The name of this site will be KidHaven.com
We will need:
1. main page design
2. site logo designed
3. subpages as well for the look of people's profiles, and job listings, etc (see links below)
We only need the design, photos, font files, etc. We do not need this site coded (no html), a ps job is fine.
Some competing sites in the space include - tendlyhub.com and vurl.com
http://www.brisk-minder.example/images/profile1.jpg
http://quenthollibrary.example/wp-content/uploads/2013/09/vurl-review.png
http://www.palvermont.example/hr/photos/tendly_hub2.jpg
Target Market(s)
Mothers of children, mainly women
Industry/Entity Type
Online
Look and feel

```html
<!DOCTYPE html>
<html lang="en">
<head>
<meta charset="utf-8">
<title>KidHaven – Home</title>
<link href="https://fonts.googleapis.com/css2?family=Lato:ital,wght@0,400;0,700;0,900;1,400;1,700&display=swap" rel="stylesheet">
<style>
:root{
  --stage:#e6e8eb;
  --white:#ffffff;
  --ink:#4a4a4a;
  --muted:#9a9a9a;
  --line:#dcdcdc;
  --orange:#d98e1f;
  --orange-dark:#b8730f;
  --green:#8cc63f;
  --grey-btn:#9a9a9a;
  --blue:#2f8fd8;
  --sky:#c4daee;
  --sky-card:rgba(190,214,238,.92);
  --btn-blue:#7fb6e6;
  --footer:#7c7c7c;
  --footer-text:#e4e4e4;
  --base:#414141;
}
*{box-sizing:border-box;margin:0;padding:0}
html,body{width:1200px;height:854px;overflow:hidden}
body{background:var(--stage);font-family:"Lato",Arial,sans-serif;color:var(--ink)}
.page{position:absolute;left:266px;top:0;width:668px;height:854px;background:var(--white);overflow:hidden}
section,header,footer,nav{position:relative}
.abs{position:absolute}

/* header */
.site-header{height:43px;border-top:2px solid var(--orange)}
.brand{left:128px;top:10px;display:flex;align-items:center;gap:5px}
.brand-dot{width:18px;height:18px;border-radius:50%;background:var(--blue)}
.brand-name{font-size:17px;font-weight:700;color:var(--blue);letter-spacing:-.2px}
.account{right:128px;top:11px;display:flex;gap:4px}
.account a{display:block;width:31px;height:10px;font-size:5px;font-weight:700;color:var(--white);text-align:center;line-height:10px;text-decoration:none;text-transform:uppercase}
.btn-signup{background:var(--green)}
.btn-login{background:var(--grey-btn)}
.social{right:128px;top:25px;display:flex;gap:3px}
.social span{width:8px;height:8px;border-radius:1px;background:#8a9bb0}

/* nav */
.main-nav{height:17px;border-top:1px solid var(--line);border-bottom:1px solid var(--line)}
.nav-list{left:128px;top:0;display:flex;list-style:none;height:16px}
.nav-list li{font-size:5.4px;color:#666;text-transform:uppercase;padding:0 6px;line-height:16px}
.nav-list li.active{background:#eeeeee;border-left:1px solid var(--line);border-right:1px solid var(--line)}
.nav-search{right:128px;top:3px;width:80px;height:10px;border:1px solid var(--line);font-size:5px;color:#aaa;padding-left:4px;line-height:8px}
.nav-search svg{position:absolute;right:2px;top:1px}

/* hero */
.hero{height:235px}
.hero-photo{left:0;top:0;width:372px;height:235px;background:linear-gradient(120deg,#c98f6c 0%,#e9c3a6 35%,#f4e3d3 60%,#e7d6c8 100%)}
.hero-room{left:372px;top:0;width:296px;height:235px;background:linear-gradient(90deg,#dfe3e6 0%,#eef0f1 45%,#c9c5bf 100%)}
.search-card{left:390px;top:18px;width:132px;height:139px;background:var(--sky-card);padding:14px 9px 0}
.search-card h2{font-size:10.5px;font-weight:700;color:var(--white);line-height:12px;margin-bottom:8px}
.field{height:15px;background:var(--white);border:1px solid #b9cde0;font-size:5px;color:#aaa;line-height:13px;padding-left:6px;margin-bottom:10px;position:relative}
.field svg{position:absolute;right:6px;top:5px}
.btn-find{width:50px;height:14px;background:var(--orange);border:1px solid var(--orange-dark);font-size:5.5px;color:var(--white);text-align:center;line-height:12px}
.signup-label{left:390px;top:179px;width:132px;text-align:center;font-size:6.5px;color:#5b5b5b;text-transform:uppercase}
.signup-label::before,.signup-label::after{content:"";position:absolute;top:4px;width:28px;height:1px;background:#b8b8b8}
.signup-label::before{left:8px}
.signup-label::after{right:8px}
.signup-btn{top:194px;height:18px;width:63px;font-size:6.5px;font-weight:700;color:var(--white);text-align:center;line-height:18px;text-transform:uppercase}
.signup-parent{left:390px;background:var(--orange)}
.signup-sitter{left:458px;background:var(--green)}

/* new sitters */
.new-sitters{height:206px;border-bottom:1px solid #eee}
.section-title{left:128px;top:18px;width:412px;text-align:center;font-size:10px;font-style:italic;font-weight:700;color:var(--orange)}
.section-title::before,.section-title::after{content:"";position:absolute;top:7px;width:148px;height:1px;background:#e2e2e2}
.section-title::before{left:0}
.section-title::after{right:0}
.arrow{top:72px}
.arrow-prev{left:136px}
.arrow-next{left:524px}
.sitter-card{top:52px;width:77px}
.sitter-photo{width:77px;height:51px;border:1px solid #d3d3d3}
.sitter-name{font-size:5.4px;font-weight:700;color:#333;margin-top:5px;padding-left:10px;position:relative}
.meta{font-size:4.8px;color:#888;padding-left:10px;position:relative;margin-top:1.5px}
.meta svg,.sitter-name svg{position:absolute;left:1px;top:0}
.bio{font-size:4.6px;line-height:6px;color:#999;margin-top:3px}
.btn-profile{display:block;width:45px;height:11px;background:var(--btn-blue);color:var(--white);font-size:5px;text-align:center;line-height:11px;margin-top:7px}

/* testimonial */
.testimonial{height:217px;background:var(--sky)}
.testimonial-bg{left:0;top:0;width:668px;height:217px;background:radial-gradient(ellipse at 40% 50%,#d7e6f3 0%,rgba(196,218,238,0) 65%)}
.quote-mark{left:128px;top:44px}
.quote{left:148px;top:47px;width:262px;font-size:14.5px;line-height:19px;font-style:italic;color:var(--white)}
.quote-author{left:156px;top:114px;font-size:8px;font-style:italic;font-weight:700;color:#8ea9c2}
.quote-role{left:156px;top:125px;font-size:5px;color:#a6bed3}
.btn-cta{left:243px;top:164px;width:90px;height:21px;background:var(--orange);border:1px solid var(--orange-dark);color:var(--white);font-size:8.5px;text-align:center;line-height:19px}
.testimonial-photo{left:418px;top:52px;width:122px;height:165px;background:linear-gradient(160deg,#f3e8df 0%,#e8c8ae 45%,#d8e6f2 100%);border-radius:55px 55px 0 0}

/* footer */
.site-footer{height:111px;background:var(--footer)}
.footer-col{top:24px;width:82px}
.footer-col h3{font-size:5.2px;font-weight:700;color:var(--white);margin-bottom:2px}
.footer-col li{list-style:none;font-size:4.6px;line-height:6.9px;color:var(--footer-text)}
.base-bar{height:25px;background:var(--base);text-align:center;font-size:4.8px;color:#cfcfcf;line-height:25px}
</style>
</head>
<body>
<div class="page">

  <header class="site-header">
    <div class="abs brand"><span class="brand-dot"></span><span class="brand-name">KidHaven</span></div>
    <div class="abs account"><a class="btn-signup" href="#">Sign up</a><a class="btn-login" href="#">Login</a></div>
    <div class="abs social"><span></span><span></span><span></span></div>
  </header>

  <nav class="main-nav">
    <ul class="abs nav-list">
      <li class="active">Home</li><li>Jobs</li><li>Sitters</li><li>How it works</li><li>Safety tips</li><li>Contact us</li>
    </ul>
    <div class="abs nav-search">Search
      <svg width="6" height="6" viewBox="0 0 10 10"><circle cx="4" cy="4" r="3" fill="none" stroke="#555" stroke-width="1.5"/><line x1="6.2" y1="6.2" x2="9.2" y2="9.2" stroke="#555" stroke-width="1.5"/></svg>
    </div>
  </nav>

  <section class="hero">
    <div class="abs hero-photo" role="img" aria-label="Photo of a smiling mother cuddling her laughing baby"></div>
    <div class="abs hero-room" role="img" aria-label="Photo of a bright, softly blurred living room"></div>
    <form class="abs search-card">
      <h2>Find an Awesome Sitter Near to You</h2>
      <div class="field">zipcode</div>
      <div class="field">ANY<svg width="5" height="3" viewBox="0 0 10 6"><path d="M0 0h10L5 6z" fill="#666"/></svg></div>
      <div class="btn-find">Find</div>
    </form>
    <div class="abs signup-label">Sign up</div>
    <div class="abs signup-btn signup-parent">As parent</div>
    <div class="abs signup-btn signup-sitter">As sitter</div>
  </section>

  <section class="new-sitters">
    <h2 class="abs section-title">New Sitters</h2>
    <svg class="abs arrow arrow-prev" width="6" height="8" viewBox="0 0 6 10"><path d="M5 1 1 5l4 4" fill="none" stroke="#b5b5b5" stroke-width="1.3"/></svg>
    <svg class="abs arrow arrow-next" width="6" height="8" viewBox="0 0 6 10"><path d="M1 1l4 4-4 4" fill="none" stroke="#b5b5b5" stroke-width="1.3"/></svg>

    <article class="abs sitter-card" style="left:157px">
      <div class="sitter-photo" role="img" aria-label="Profile photo of sitter Mirela T." style="background:linear-gradient(135deg,#9fcf6a,#d9c2a8)"></div>
      <div class="sitter-name"><svg width="5" height="6" viewBox="0 0 10 12"><circle cx="5" cy="3.5" r="2.8" fill="#999"/><path d="M0 12c0-4 10-4 10 0z" fill="#999"/></svg>Mirela T.</div>
      <div class="meta"><svg width="5" height="6" viewBox="0 0 10 12"><path d="M5 0a4 4 0 0 1 4 4c0 3-4 8-4 8S1 7 1 4a4 4 0 0 1 4-4z" fill="#999"/></svg>San Francisco, CA</div>
      <div class="meta"><svg width="5" height="6" viewBox="0 0 10 12"><text x="2" y="10" font-size="11" fill="#999">$</text></svg>$12-$18 / hour</div>
      <p class="bio">Caring sitter with years of infant and toddler experience, first aid certified, loves crafts and outdoor play.</p>
      <span class="btn-profile">View Profile</span>
    </article>

    <article class="abs sitter-card" style="left:250px">
      <div class="sitter-photo" role="img" aria-label="Profile photo of sitter Jonelle P." style="background:linear-gradient(135deg,#caa48a,#6f4a35)"></div>
      <div class="sitter-name"><svg width="5" height="6" viewBox="0 0 10 12"><circle cx="5" cy="3.5" r="2.8" fill="#999"/><path d="M0 12c0-4 10-4 10 0z" fill="#999"/></svg>Jonelle P.</div>
      <div class="meta"><svg width="5" height="6" viewBox="0 0 10 12"><path d="M5 0a4 4 0 0 1 4 4c0 3-4 8-4 8S1 7 1 4a4 4 0 0 1 4-4z" fill="#999"/></svg>Miami, FL</div>
      <div class="meta"><svg width="5" height="6" viewBox="0 0 10 12"><text x="2" y="10" font-size="11" fill="#999">$</text></svg>$15-$20 / hour</div>
      <p class="bio">Caring sitter with years of infant and toddler experience, first aid certified, loves crafts and outdoor play.</p>
      <span class="btn-profile">View Profile</span>
    </article>

    <article class="abs sitter-card" style="left:343px">
      <div class="sitter-photo" role="img" aria-label="Profile photo of sitter Brynn A." style="background:linear-gradient(135deg,#e8e2d8,#d9b77e)"></div>
      <div class="sitter-name"><svg width="5" height="6" viewBox="0 0 10 12"><circle cx="5" cy="3.5" r="2.8" fill="#999"/><path d="M0 12c0-4 10-4 10 0z" fill="#999"/></svg>Brynn A.</div>
      <div class="meta"><svg width="5" height="6" viewBox="0 0 10 12"><path d="M5 0a4 4 0 0 1 4 4c0 3-4 8-4 8S1 7 1 4a4 4 0 0 1 4-4z" fill="#999"/></svg>Los Angeles, CA</div>
      <div class="meta"><svg width="5" height="6" viewBox="0 0 10 12"><text x="2" y="10" font-size="11" fill="#999">$</text></svg>$12-$18 / hour</div>
      <p class="bio">Caring sitter with years of infant and toddler experience, first aid certified, loves crafts and outdoor play.</p>
      <span class="btn-profile">View Profile</span>
    </article>

    <article class="abs sitter-card" style="left:436px">
      <div class="sitter-photo" role="img" aria-label="Profile photo of sitter Tamsin V." style="background:linear-gradient(135deg,#b58c74,#4a2f27)"></div>
      <div class="sitter-name"><svg width="5" height="6" viewBox="0 0 10 12"><circle cx="5" cy="3.5" r="2.8" fill="#999"/><path d="M0 12c0-4 10-4 10 0z" fill="#999"/></svg>Tamsin V.</div>
      <div class="meta"><svg width="5" height="6" viewBox="0 0 10 12"><path d="M5 0a4 4 0 0 1 4 4c0 3-4 8-4 8S1 7 1 4a4 4 0 0 1 4-4z" fill="#999"/></svg>Austin, TX</div>
      <div class="meta"><svg width="5" height="6" viewBox="0 0 10 12"><text x="2" y="10" font-size="11" fill="#999">$</text></svg>$14-$18 / hour</div>
      <p class="bio">Caring sitter with years of infant and toddler experience, first aid certified, loves crafts and outdoor play.</p>
      <span class="btn-profile">View Profile</span>
    </article>
  </section>

  <section class="testimonial">
    <div class="abs testimonial-bg"></div>
    <svg class="abs quote-mark" width="17" height="13" viewBox="0 0 34 26"><path d="M0 26V14C0 6 4 1 12 0v5c-4 1-6 4-6 8h6v13zm20 0V14c0-8 4-13 12-14v5c-4 1-6 4-6 8h6v13z" fill="#e6eff7"/></svg>
    <blockquote class="abs quote">kidhaven.com is the best place to find great quality sitters and the website is so easy to use!”</blockquote>
    <div class="abs quote-author">Delia Marsh</div>
    <div class="abs quote-role">Mother of two, Portland</div>
    <div class="abs btn-cta">Find a Sitter Now</div>
    <div class="abs testimonial-photo" role="img" aria-label="Photo of a young mother holding up her baby"></div>
  </section>

  <footer class="site-footer">
    <div class="abs footer-col" style="left:128px">
      <h3>Discover</h3>
      <ul><li>How It Works</li><li>Testimonials</li><li>Local Events</li><li>Gift Cards</li><li>Childcare Resources</li><li>Download the App</li><li>Careers at KidHaven</li></ul>
    </div>
    <div class="abs footer-col" style="left:212px">
      <h3>Company</h3>
      <ul><li>About Us</li><li>Press</li><li>FAQs &amp; Support</li><li>Terms of Service</li><li>Privacy Policy</li></ul>
    </div>
    <div class="abs footer-col" style="left:295px">
      <h3>Babysitters</h3>
      <ul><li>San Francisco Babysitters</li><li>New York City Babysitters</li><li>Chicago Babysitters</li><li>Los Angeles Babysitters</li><li>Seattle Babysitters</li><li>Washington DC Babysitters</li><li>Boston Babysitters</li><li>Denver Babysitters</li><li>San Diego Babysitters</li></ul>
    </div>
    <div class="abs footer-col" style="left:379px">
      <h3>Nannies</h3>
      <ul><li>San Francisco Nannies</li><li>New York City Nannies</li><li>Chicago Nannies</li><li>Los Angeles Nannies</li><li>Seattle Nannies</li><li>Washington DC Nannies</li><li>Boston Nannies</li><li>Denver Nannies</li><li>San Diego Nannies</li></ul>
    </div>
    <div class="abs footer-col" style="left:462px">
      <h3>More Services</h3>
      <ul><li>Find Special Needs Care</li><li>Find Care Companions</li><li>Find Pet Sitters</li></ul>
    </div>
  </footer>
  <div class="base-bar">© KidHaven. All Rights Reserved.</div>

</div>
</body>
</html>
```